Youtube Thumbnail templates x 4 for football channel (more than 1 winner will be chosen)

I am looking for a set of 4 thumbnail templates that are on brand.

They should be eye catching and baiting the click.

The 4 different thumbnails will likely be very similar.

It is highly likely that I will choose more than 1 designer as the winner for the project

I have added my brand guidelines below as well as my logo.

The website page to get a good feel for my brand is: https://brightpitch.example/434-coaching/

Also, please feel free to add any images of famous footballers in the template, as these will be delivered in PSD file at the end I will be able to edit these thumbnails before they go live

Target Market(s)

Football players of all levels

Font styles to use
Sans Serif

Requirements
Must have
• Be on brand.
Be eye catching and very clickable

```html
<!DOCTYPE html>
<html lang="en">
<head>
<meta charset="utf-8">
<title>Steady Striker – Thumbnail Templates</title>
<link rel="stylesheet" href="https://fonts.googleapis.com/css2?family=Montserrat:wght@600;700;800&display=swap">
<style>
  :root {
    --page-bg: #ffffff;
    --ink-dark: #1f2022;
    --ink-grey: #343537;
    --brand-blue: #174a92;
    --deep-blue: #0f3470;
    --bright-blue: #2566c2;
    --sky-blue: #3aa6e2;
    --stripe-grey: #8a8b8d;
    --white: #ffffff;
  }
  html, body {
    margin: 0;
    padding: 0;
    width: 720px;
    height: 1200px;
    overflow: hidden;
    background: var(--page-bg);
  }
  .sheet {
    position: relative;
    width: 720px;
    height: 1200px;
  }
  .thumbnail {
    position: absolute;
    left: 149px;
    width: 424px;
    height: 238px;
    box-shadow: 0 10px 18px rgba(0,0,0,0.28);
  }
  .thumbnail svg {
    display: block;
    width: 100%;
    height: 100%;
  }
  .thumbnail--one   { top: 38px; }
  .thumbnail--two   { top: 332px; }
  .thumbnail--three { top: 627px; }
  .thumbnail--four  { top: 922px; }

  .brand-name   { font-family: "Montserrat", sans-serif; font-weight: 700; font-size: 19px; fill: var(--white); letter-spacing: 0.5px; }
  .headline-lead { font-family: "Montserrat", sans-serif; font-weight: 800; font-size: 40px; fill: var(--sky-blue); }
  .headline-main { font-family: "Montserrat", sans-serif; font-weight: 800; fill: var(--white); }
  .headline-main--brain { font-size: 76px; }
  .headline-main--game  { font-size: 62px; }
</style>
</head>
<body>
<main class="sheet">

  <!-- Template 1 -->
  <section class="thumbnail thumbnail--one">
    <svg viewBox="0 0 706 397" xmlns="http://www.w3.org/2000/svg">
      <defs>
        <linearGradient id="player-tone" x1="0" y1="0" x2="1" y2="1">
          <stop offset="0" stop-color="#9c9c9c"/>
          <stop offset="0.5" stop-color="#6e6e6e"/>
          <stop offset="1" stop-color="#c9c9c9"/>
        </linearGradient>
      </defs>
      <rect class="backdrop" width="706" height="397" fill="var(--ink-dark)"/>
      <polygon class="blue-panel" points="455,0 706,0 706,270 540,397 420,397 300,230" fill="var(--brand-blue)"/>
      <polygon class="blue-corner" points="0,295 0,397 115,397" fill="var(--brand-blue)"/>
      <g class="speed-stripes">
        <polygon points="290,235 302,235 470,397 458,397" fill="var(--stripe-grey)"/>
        <polygon points="255,275 262,275 395,397 388,397" fill="none" stroke="var(--stripe-grey)" stroke-width="1.5"/>
        <polygon points="310,262 318,262 450,397 442,397" fill="var(--stripe-grey)" opacity="0.6"/>
      </g>
      <rect class="player-photo" role="img" aria-label="Black and white photo of a footballer dribbling a ball" x="355" y="15" width="340" height="382" rx="40" fill="url(#player-tone)"/>
      <g class="brand-mark">
        <circle cx="48" cy="57" r="19" fill="none" stroke="var(--white)" stroke-width="3"/>
        <text class="brand-name" x="75" y="52">STEADY</text>
        <text class="brand-name" x="75" y="73">STRIKER</text>
      </g>
      <text class="headline-lead" x="28" y="150">USE YOUR</text>
      <text class="headline-main headline-main--brain" x="26" y="212">BRAIN</text>
      <text class="headline-lead" x="28" y="252">RAISE YOUR</text>
      <text class="headline-main headline-main--game" x="26" y="302">GAME</text>
    </svg>
  </section>

  <!-- Template 2 -->
  <section class="thumbnail thumbnail--two">
    <svg viewBox="0 0 706 397" xmlns="http://www.w3.org/2000/svg">
      <defs>
        <linearGradient id="player-tone-2" x1="0" y1="0" x2="1" y2="1">
          <stop offset="0" stop-color="#9c9c9c"/>
          <stop offset="0.5" stop-color="#6e6e6e"/>
          <stop offset="1" stop-color="#c9c9c9"/>
        </linearGradient>
      </defs>
      <rect class="backdrop" width="706" height="397" fill="var(--ink-grey)"/>
      <polygon class="blue-panel" points="470,0 706,0 706,397 190,397" fill="var(--brand-blue)"/>
      <polygon class="blue-flash" points="520,35 706,95 706,145 465,62" fill="var(--bright-blue)"/>
      <g class="speed-stripes">
        <polygon points="180,290 190,290 105,397 95,397" fill="var(--stripe-grey)"/>
        <polygon points="255,245 265,245 145,397 135,397" fill="none" stroke="var(--stripe-grey)" stroke-width="1.5"/>
        <polygon points="205,290 212,290 120,397 113,397" fill="var(--stripe-grey)" opacity="0.6"/>
      </g>
      <rect class="player-photo" role="img" aria-label="Black and white photo of a footballer dribbling a ball" x="355" y="15" width="340" height="382" rx="40" fill="url(#player-tone-2)"/>
      <g class="brand-mark">
        <circle cx="48" cy="47" r="19" fill="none" stroke="var(--white)" stroke-width="3"/>
        <text class="brand-name" x="75" y="42">STEADY</text>
        <text class="brand-name" x="75" y="63">STRIKER</text>
      </g>
      <text class="headline-lead" x="28" y="125">USE YOUR</text>
      <text class="headline-main headline-main--brain" x="26" y="187">BRAIN</text>
      <text class="headline-lead" x="28" y="227">RAISE YOUR</text>
      <text class="headline-main headline-main--game" x="26" y="277">GAME</text>
    </svg>
  </section>

  <!-- Template 3 -->
  <section class="thumbnail thumbnail--three">
    <svg viewBox="0 0 706 397" xmlns="http://www.w3.org/2000/svg">
      <defs>
        <linearGradient id="player-tone-3" x1="0" y1="0" x2="1" y2="1">
          <stop offset="0" stop-color="#9c9c9c"/>
          <stop offset="0.5" stop-color="#6e6e6e"/>
          <stop offset="1" stop-color="#c9c9c9"/>
        </linearGradient>
        <linearGradient id="stadium-blue-3" x1="0" y1="0" x2="0" y2="1">
          <stop offset="0" stop-color="var(--brand-blue)"/>
          <stop offset="1" stop-color="var(--deep-blue)"/>
        </linearGradient>
      </defs>
      <rect class="backdrop" width="706" height="397" fill="var(--ink-dark)"/>
      <polygon class="blue-band" points="95,0 500,0 482,35 80,35" fill="var(--deep-blue)"/>
      <polygon class="blue-panel" points="30,52 450,52 300,397 0,397 0,120" fill="url(#stadium-blue-3)"/>
      <g class="speed-stripes">
        <polygon points="420,205 445,210 340,397 318,397" fill="none" stroke="var(--white)" stroke-width="2"/>
        <polygon points="438,255 455,258 380,397 365,397" fill="var(--white)" opacity="0.9"/>
        <polygon points="478,260 488,262 405,397 397,397" fill="none" stroke="var(--white)" stroke-width="1.5"/>
      </g>
      <rect class="player-photo" role="img" aria-label="Black and white photo of a footballer dribbling a ball" x="355" y="15" width="340" height="382" rx="40" fill="url(#player-tone-3)"/>
      <g class="brand-mark">
        <circle cx="120" cy="103" r="19" fill="none" stroke="var(--white)" stroke-width="3"/>
        <text class="brand-name" x="147" y="98">STEADY</text>
        <text class="brand-name" x="147" y="119">STRIKER</text>
      </g>
      <g text-anchor="middle">
        <text class="headline-lead" x="188" y="175">USE YOUR</text>
        <text class="headline-main headline-main--brain" x="188" y="242">BRAIN</text>
        <rect class="divider" x="160" y="260" width="56" height="4" fill="var(--sky-blue)"/>
        <text class="headline-lead" x="188" y="312">RAISE YOUR</text>
        <text class="headline-main headline-main--game" x="188" y="370">GAME</text>
      </g>
    </svg>
  </section>

  <!-- Template 4 -->
  <section class="thumbnail thumbnail--four">
    <svg viewBox="0 0 706 397" xmlns="http://www.w3.org/2000/svg">
      <defs>
        <linearGradient id="player-tone-4" x1="0" y1="0" x2="1" y2="1">
          <stop offset="0" stop-color="#9c9c9c"/>
          <stop offset="0.5" stop-color="#6e6e6e"/>
          <stop offset="1" stop-color="#c9c9c9"/>
        </linearGradient>
        <linearGradient id="stadium-blue-4" x1="0" y1="0" x2="0" y2="1">
          <stop offset="0" stop-color="var(--brand-blue)"/>
          <stop offset="1" stop-color="var(--deep-blue)"/>
        </linearGradient>
      </defs>
      <rect class="backdrop" width="706" height="397" fill="var(--ink-dark)"/>
      <polygon class="blue-panel" points="0,0 310,0 480,397 0,397" fill="url(#stadium-blue-4)"/>
      <polygon class="dark-corner" points="0,330 0,397 40,397" fill="var(--ink-dark)"/>
      <g class="speed-stripes">
        <polygon points="330,0 345,0 475,255 458,255" fill="none" stroke="var(--white)" stroke-width="2"/>
        <polygon points="410,0 440,0 580,250 550,250" fill="none" stroke="var(--white)" stroke-width="2"/>
        <polygon points="430,0 452,0 490,75 470,75" fill="var(--white)" opacity="0.9"/>
      </g>
      <rect class="player-photo" role="img" aria-label="Black and white photo of a footballer dribbling a ball" x="355" y="15" width="340" height="382" rx="40" fill="url(#player-tone-4)"/>
      <g class="brand-mark">
        <circle cx="115" cy="64" r="19" fill="none" stroke="var(--white)" stroke-width="3"/>
        <text class="brand-name" x="142" y="59">STEADY</text>
        <text class="brand-name" x="142" y="80">STRIKER</text>
      </g>
      <g text-anchor="middle">
        <text class="headline-lead" x="188" y="145">USE YOUR</text>
        <text class="headline-main headline-main--brain" x="188" y="212">BRAIN</text>
        <rect class="divider" x="160" y="233" width="56" height="4" fill="var(--sky-blue)"/>
        <text class="headline-lead" x="188" y="282">RAISE YOUR</text>
        <text class="headline-main headline-main--game" x="188" y="340">GAME</text>
      </g>
    </svg>
  </section>

</main>
</body>
</html>
```